Word Template for KOREL Polls

KOREL Polls stands for 'Kindred Outlook Readings Entered Locally Polls'. It is a collaborative research effort to format and combine multiple sources of public opinion data from around the world into merged datasets. We need a Microsoft Word template design for our research reports, dataset codebooks, crowdsourced development guidelines, and other documents that will be produced as part of the research and development. The template should match the website design and logo, which are attached to this contest (these are the files from previous successful design contests).

The main purpose will be to write reports discussing research and analysis. There will be lots data visualizations (bar charts, scatter plots, pie charts, histograms, trend line charts etc.) as well as tables, diargams, and photos mixed in wit all the text. A second purpose will be to write guidebooks to describe processes and teach others how to manage data, find variables, and write code, which will include screenshots and Word are diagrams and figures.

There are some document uploaded as examples for the kinds of things for which we need the template (working papers, codebooks, pamphlets, etc)

Target Market(s)

academia, government, non-profits, postgraduates, researchers

Font styles to use
Serif

Colors

Designer to choose colors to be used in the design.

Requirements
Must have
• A4 size page template
• Cover page
• Must match website design and logo (see attached)
Nice to have
• Colors to match logo and website (see attached)

```html
<!DOCTYPE html>
<html lang="en">
<head>
<meta charset="utf-8">
<title>KOREL Polls – Report Page</title>
<link href="https://fonts.googleapis.com/css2?family=Roboto:wght@400;500;700&display=swap" rel="stylesheet">
<style>
:root{
  --blue:#2a93dd;
  --blue-dark:#155fa8;
  --text:#3a3a3a;
  --heading:#1e1e1e;
  --paper:#ffffff;
}
*{margin:0;padding:0;box-sizing:border-box}
html,body{width:848px;height:1200px;overflow:hidden;background:var(--paper)}
body{font-family:'Roboto',Arial,sans-serif;color:var(--text);position:relative}
.header-band{position:absolute;left:0;top:0;width:848px;height:98px;
  background:linear-gradient(90deg,#1b7fca 0%,#2a96e0 45%,#1f8ad6 70%,#1870b8 100%)}
.brand{position:absolute;top:0;left:0;width:848px;height:98px;display:flex;align-items:center;justify-content:center;gap:12px}
.brand-dot{width:34px;height:34px;border-radius:50%;border:3px solid #fff}
.brand-name{color:#fff;font-size:32px;font-weight:500;letter-spacing:.2px}
.body-text{position:absolute;font-size:8.6px;line-height:17.1px;text-align:justify;letter-spacing:-.05px}
.intro{left:34px;top:140px;width:781px}
.funding{left:34px;top:277px;width:480px;letter-spacing:-.12px}
.indicators{left:34px;top:536px;width:781px}
.section-title{position:absolute;left:33px;top:688px;font-size:22.5px;font-weight:700;color:var(--heading);letter-spacing:-.1px}
.globalization{left:33px;top:738px;width:781px}
.inequality{left:258px;top:868px;width:556px}
.corruption{left:33px;top:1080px;width:781px}
.globe-figure{position:absolute;left:30px;top:870px;width:205px;height:180px;border-radius:50%;
  background:radial-gradient(circle at 45% 40%,#e9eef5 0%,#b9c7da 55%,#6f84a3 100%)}
.trend-chart{position:absolute;left:540px;top:280px;width:290px;height:230px}
.page-number{position:absolute;left:822px;top:1170px;font-size:7px;color:#555}
.footer-band{position:absolute;left:0;top:1190px;width:848px;height:10px;background:var(--blue-dark)}
.footer-band::before{content:"";position:absolute;left:0;top:0;width:420px;height:10px;background:var(--blue);
  clip-path:polygon(0 0,100% 0,calc(100% - 8px) 100%,0 100%)}
</style>
</head>
<body>
<header class="header-band" role="img" aria-label="Blue-toned photograph of people taking part in a survey"></header>
<div class="brand"><span class="brand-dot"></span><span class="brand-name">KOREL Polls</span></div>

<p class="body-text intro">There are additional challenges when working with multiple data sources, such as contending with different survey answer scales and survey designs. However, there are also many benefits to cross-survey research that outweigh these challenges when properly accounting for them. For example, using multiple sources provides greater variation and enables answering new research questions. The merged respondent level dataset includes millions of individuals from most countries in the world and extends back decades. This enables tracking trends over time, repeating models across different surveys, and increasing the reliability and generalisability of findings. It is also possible to run parallel models across different survey rounds and source using the original survey items to uncover broad patterns. Yet the advantages come with a cost measured in time managing data. Each survey dataset requires cleaning and formatting before running parallel models or undertaking any analysis, and there are thousands of datasets. The data management required is a substantial barrier to doing cross-survey research, which often requires a well-funded research team. Financial cost is therefore another barrier to doing cross-survey research.</p>

<p class="body-text funding">A team of sociologists based jointly at the Vessen Academy of Sciences and Lakemont State University have won multiple rounds of research funding worth millions of Euros to harmonize multiple sources of survey data (Varnel &amp; Tamsin-Varnel, 2016; Tamsin-Varnel &amp; Pelkowitz, 2016). Despite this substantial funding, the team has formatted a fraction of the available sources and variables. The project also uses a suite of customised software tools requiring expert knowledge and paid database specialists to manage the technical aspects of the projects (Dornik &amp; Salwiak, 2016). This is a logical approach and it has numerous advantages, but it places this kind of work beyond the capabilities of most social scientists. It means that anyone wishing to expand the resource must first learn specialized programming languages and database management software in addition to statistical analysis software. The funding pays people with the required software skills, which means that when the funding disappears the project may stop harmonizing public surveys. KOREL Polls takes a crowdsourced approach to the same problem using only Tabulo, a statistics software package than many social scientists already know how to use. Comparative public opinion researchers already spend countless hours working ‘for free’ cleaning up survey datasets before analysing them. We separately repeat the same steps on the same datasets, redundantly doing work that somebody else has already done and others will repeat in the future. The idea behind KOREL Polls is to operate indefinitely without substantial funding and collectively expand the number of included sources and variables.</p>

<svg class="trend-chart" viewBox="540 280 290 230" xmlns="http://www.w3.org/2000/svg" font-family="Roboto, Arial, sans-serif" font-size="7" fill="#444">
  <g stroke="#e2e2e2" stroke-dasharray="3 3" stroke-width="0.8">
    <line x1="570" y1="456" x2="818" y2="456"/>
    <line x1="570" y1="430" x2="818" y2="430"/>
    <line x1="570" y1="404" x2="818" y2="404"/>
    <line x1="570" y1="378" x2="818" y2="378"/>
    <line x1="570" y1="352" x2="818" y2="352"/>
    <line x1="570" y1="326" x2="818" y2="326"/>
    <line x1="570" y1="300" x2="818" y2="300"/>
  </g>
  <line x1="570" y1="292" x2="570" y2="482" stroke="#ccc" stroke-width="0.8"/>
  <line x1="570" y1="482" x2="818" y2="482" stroke="#ccc" stroke-width="0.8"/>
  <g text-anchor="end">
    <text x="563" y="485">0</text><text x="563" y="459">5K</text><text x="563" y="433">10K</text>
    <text x="563" y="407">15K</text><text x="563" y="381">20K</text><text x="563" y="355">25K</text><text x="563" y="329">30K</text>
  </g>
  <g fill="#2a93dd">
    <rect x="575" y="401" width="11" height="81"/><rect x="610" y="356" width="11" height="126"/>
    <rect x="646" y="356" width="11" height="126"/><rect x="681" y="318" width="11" height="164"/>
    <rect x="716" y="367" width="11" height="115"/><rect x="752" y="344" width="11" height="138"/>
    <rect x="787" y="310" width="11" height="172"/>
  </g>
  <g fill="#155fa8">
    <rect x="588" y="383" width="11" height="99"/><rect x="623" y="348" width="11" height="134"/>
    <rect x="659" y="398" width="11" height="84"/><rect x="694" y="348" width="11" height="134"/>
    <rect x="729" y="425" width="11" height="57"/><rect x="765" y="406" width="11" height="76"/>
    <rect x="800" y="392" width="11" height="90"/>
  </g>
  <rect x="607" y="316" width="28" height="13" rx="2" fill="#fff" stroke="#ddd" stroke-width="0.6"/>
  <text x="621" y="325" text-anchor="middle" font-size="6" font-weight="700" fill="#333">14.2K</text>
  <g text-anchor="middle" font-size="6.5" font-weight="500">
    <text x="587" y="495">Mon</text><text x="622" y="495">Tue</text><text x="658" y="495">Wed</text>
    <text x="693" y="495">Thu</text><text x="728" y="495">Fri</text><text x="764" y="495">Sat</text><text x="799" y="495">Sun</text>
  </g>
</svg>

<p class="body-text indicators">One of the uses of formatted and merged respondent level data is to create national level public opinion indicators. Some examples are already included within the standard Civic Standards (CSI) country-year dataset. For example, Lindqvar et al. (2018) provide country average scores calculated using the population weights in the Meridian Values Panel and Continental Values Study data to measure trust in different institutions. They also provide average country scores for satisfaction with democracy using the Cross-National Ballot Study and additional trust in political institution indicators using the Continental Values Study (Lindqvar et al., 2018). Hanzer (2013) similarly constructed national-level indicators of trust in political institutions and generalized social trust with data from the Meridian Values Panel. However, these measures rescaled individual responses to range from 0.0 for no trust to 1.0 for the most trust and then averaged these values within national samples (Hanzer, 2013). Averaging approaches may differ slightly, but they avoid discarding data. This study explains the construction of national public opinion indices and applies them to analysing the effects of globalization, inequality, and corruption.</p>

<h2 class="section-title">1.1. EFFECTS OF GLOBALIZATION, INEQUALITY, AND CORRUPTION</h2>

<p class="body-text globalization">This paper analyses three indices measuring national conditions for their effects on aggregated public opinion indices. First, an economic globalisation index measures the international flow of goods and services as well as trade restrictions such as tariffs or investment limitations (Kessling, 2006; Brann, Oelk, &amp; Marder, 2018). The assumption is that globalization has differing effects of different socioeconomic groups. Many multinational firms have gradually moved their production from more developed to less developed countries, leaving workers in affected industries with less job security and lower incomes (Trevan &amp; Moss, 2004). Many lower skilled jobs requiring less education have been moving from countries with higher labour costs to countries with lower labour costs. The consequences for people with lower education in developed countries would be less financial security than people with more education (Halden, Rusk, &amp; Pryor, 2013). This economic insecurity is hypothesised to translate into relatively more negative attitudes towards democracy and elections for lower socioeconomic groups than for higher socioeconomic groups.</p>

<div class="globe-figure" role="img" aria-label="Illustration of a globe drawn as a network of connected points"></div>

<p class="body-text inequality">The distribution of income within societies can also be important for public opinion. Principles of fairness are important for democracy and unjust outcomes such as wide income inequalities are associated with popular dissatisfaction and lower political support (Ashby &amp; Stern, 2008; Mauder, 1988; Sorel, Marchetti, &amp; Valdi, 2014). Higher income individuals also tend to show more positive attitudes towards democracy than poorer people in the same countries (Ashby &amp; Gallo, 1997; Berndt &amp; Vossel, 2012; Kerwin &amp; Clavel, 1994; Walder-Moyne, 1999; Welland &amp; Kreis, 2006). The causal mechanisms are likely to include that wealthier individuals tend to have better standards of living, live in safer neighbourhoods, and have more political influence than poorer individuals. Economically disadvantaged groups are often more affected by economic downturns, but they are also more likely to support violent protests (Corvin &amp; Selwyn, 2010). As income inequality increases in a society and more wealth concentrates within a smaller minority, the absolute number of economically disadvantaged increases. These groups are often more affected by economic downturns and more likely to support violent protests (Corvin &amp; Selwyn, 2010). Societies with greater income inequality also have lower levels of social trust and higher rates of violent crime (Elston &amp; Aiken, 2011). The hypothesis is that income inequality will have negative effect on the measures of public opinion in this study.</p>

<p class="body-text corruption">A substantial body of literature indicates that corruption tends to have a negative effect political and social trust around the world (Chen &amp; Cho, 2006; Maar &amp; Hovsepian, 2017; Selwyn, 2002; Wegner, Schnell, &amp; Hall, 2009). It can be more important that the electoral system for perceptions of electoral fairness and more important than institutional quality for satisfaction with democracy (Donnell &amp; Karsten, 2017; McAlder &amp; Whitby, 2015; McCrae &amp; Dominick, 1998). Corruption in governance is expected to have a negative effect on the public opinion measures in this study.</p>

<span class="page-number">c7</span>
<footer class="footer-band"></footer>
</body>
</html>
```